Harlow Ironworks Business Card

We need a business card design for a new small metal fabrication business in rural NSW, Australia.

The business (Harlow Ironworks) is owner operated by a man with the initials KB - much of the branding comes from this name.

Harlow Ironworks designs, engineers, repairs and manufactures a range of custom, quality metal works including vehicle trays, agricultural machinery impliments, trailers, wood splitters, fire pits, furniture etc.

The brand position focuses on custom work of the highest quality.

Business card design should show quality, attention to detail and stand out among a mass of business cards.

Logos are in the files

The grey color may be changed on the logo if required to stand out more.

There is an image attached of a simple card that is liked because it is clean, clear, simple, masculine and effective. It says 'quality'. As most of the work we do is custom it would be good to have the business card speak to this.

Target Market(s)

Rural and regional based Australians. Primarily adult male 25-60 yrs. Primary production / rural / travelling lifestyle.

Industry/Entity Type

Metal Fabrication

Contact Information for Business Card

The words 'custom quality fabrications' would be great somewhere perhaps on the backside (not on the information side)
Name
title
Phone: 0418 539 746 and (02) 6193 4827
email: info@harlowiw.com.au
www.harlowiw.com.au

address (2 lines)

Requirements
Nice to have
• Background colour should be very navy blue or black.
Should not have
• NO orange and blue combinations.
• Navy is OK

```html
<!DOCTYPE html>
<html lang="en">
<head>
<meta charset="utf-8">
<title>Harlow Ironworks Business Card</title>
<link href="https://fonts.googleapis.com/css2?family=Pathway+Gothic+One&family=Michroma&display=swap" rel="stylesheet">
<style>
  :root {
    --canvas: #ffffff;
    --green: #7ab317;
    --green-deep: #639613;
    --black: #000000;
    --grey: #a8a5a2;
    --white: #ffffff;
    --label: #c9c9c9;
  }
  * { margin: 0; padding: 0; box-sizing: border-box; }
  html, body {
    width: 1200px; height: 801px; overflow: hidden;
    background: var(--canvas);
  }
  body { position: relative; font-family: "Pathway Gothic One", sans-serif; }

  .card { position: absolute; left: 361px; width: 489px; height: 316px; overflow: hidden; }

  /* Card back */
  .card-back { top: 76px; background: var(--green); }
  .card-back .brand-mark {
    position: absolute; left: 0; right: 0; top: 138px;
    text-align: center; color: var(--green-deep);
    font-family: "Michroma", sans-serif; font-size: 22px; letter-spacing: 1px;
  }

  /* Card front */
  .card-front { top: 414px; background: var(--black); }
  .info-side { position: absolute; left: 0; top: 0; width: 342px; height: 100%; }
  .brand {
    position: absolute; left: 22px; top: 29px;
    display: flex; align-items: center; gap: 8px;
    color: var(--grey); font-family: "Michroma", sans-serif; font-size: 15px; letter-spacing: 0.5px;
  }
  .brand-square { width: 30px; height: 30px; background: var(--grey); }
  .accent-rule {
    position: absolute; left: 0; top: 88px; width: 249px; height: 5px;
    background: var(--green);
    clip-path: polygon(0 0, 96% 0, 100% 100%, 0 100%);
  }
  .person-name { position: absolute; left: 31px; top: 114px; color: var(--white); font-size: 30px; }
  .person-title { position: absolute; left: 31px; top: 160px; color: var(--label); font-size: 23px; }
  .contact { position: absolute; left: 31px; top: 196px; list-style: none; font-size: 18px; color: var(--label); }
  .contact li { height: 31px; }
  .contact .value { color: var(--white); }

  .tagline-side {
    position: absolute; left: 342px; top: 0; width: 147px; height: 100%;
    background: var(--green);
  }
  .tagline {
    position: absolute; left: 29px; top: 40px;
    writing-mode: vertical-rl; color: var(--green-deep);
    font-size: 25px; line-height: 1;
  }
  .side-brand {
    position: absolute; left: 66px; top: 34px;
    writing-mode: vertical-rl; color: var(--green-deep);
    font-family: "Michroma", sans-serif; font-size: 19px; line-height: 1.1;
  }
</style>
</head>
<body>
  <section class="card card-back">
    <div class="brand-mark">Harlow Ironworks</div>
  </section>

  <section class="card card-front">
    <div class="info-side">
      <div class="brand"><span class="brand-square"></span><span>Harlow Ironworks</span></div>
      <div class="accent-rule"></div>
      <h1 class="person-name">K. Brennan</h1>
      <p class="person-title">Design Engineer</p>
      <ul class="contact">
        <li>Phone: <span class="value">0418 539 746</span> and <span class="value">(02) 6193 4827</span></li>
        <li>Email: <span class="value">info@harlowiw.com.au</span></li>
        <li>Web: <span class="value">www.harlowiw.com.au</span></li>
      </ul>
    </div>
    <div class="tagline-side">
      <p class="tagline">Custom Quality Fabrications</p>
      <p class="side-brand">Harlow Ironworks</p>
    </div>
  </section>
</body>
</html>
```